World Wide News and Current Affairs website

We intends to start up a new website which deals on New and Current Affairs.
Attention Designers,
We want a home page design for this project. Our business is based in the United States. Our goal is to become a well known brand.
The website would consist of a category for News, Business and Tech.
The theme should be beautiful and attention seeking. The website would take bulk of it's news from the US, and Europe.
Designers can get inspiration from already existing new websites such as HVZ, FQJ, DORNAKE.
All designs should be clean and easy to navigate.

```html
<!DOCTYPE html>
<html lang="en">
<head>
<meta charset="utf-8">
<title>Home</title>
<link href="https://fonts.googleapis.com/css2?family=Montserrat:wght@400;700&family=Merriweather:wght@700&display=swap" rel="stylesheet">
<style>
  :root {
    --header-bg: #232627;
    --nav-active-bg: #2c2f30;
    --accent: #f7941d;
    --text: #ffffff;
    --divider: #4a5560;
  }
  * { margin: 0; padding: 0; box-sizing: border-box; }
  html, body { width: 1200px; height: 377px; overflow: hidden; background: var(--header-bg); }
  body { font-family: 'Montserrat', sans-serif; color: var(--text); position: relative; }

  .site-header { position: absolute; left: 0; top: 0; width: 1200px; height: 44px; background: var(--header-bg); }
  .brand { position: absolute; left: 262px; top: 5px; font-family: 'Montserrat', sans-serif; font-weight: 700; font-size: 29px; color: var(--accent); letter-spacing: 0.5px; }
  .main-nav { position: absolute; left: 628px; top: 0; height: 44px; display: flex; }
  .main-nav a { display: block; height: 44px; line-height: 44px; font-size: 8.5px; font-weight: 700; letter-spacing: 0.8px; color: var(--text); text-decoration: none; text-align: center; }
  .main-nav .is-active { width: 65px; background: var(--nav-active-bg); border-bottom: 2px solid var(--accent); line-height: 42px; }
  .main-nav .nav-news { width: 66px; }
  .main-nav .nav-about { width: 88px; }
  .main-nav .nav-contact { width: 96px; }

  .story-grid { position: absolute; left: 0; top: 44px; width: 1200px; height: 333px; }
  .story { position: absolute; overflow: hidden; }
  .story-media { position: absolute; inset: 0; }
  .story-date { position: absolute; font-size: 10.5px; }
  .story-title { position: absolute; font-family: 'Merriweather', serif; font-weight: 700; line-height: 1.22; }
  .story-excerpt { position: absolute; font-size: 10.5px; line-height: 13px; }
  .story-byline { position: absolute; font-size: 8.5px; }
  .story-byline span { color: var(--accent); }

  .story--lead { left: 0; top: 0; width: 652px; height: 333px; }
  .story--lead .story-media { background: linear-gradient(135deg, #3b4556 0%, #2a3140 45%, #1d2330 100%); }
  .story--lead .story-date { left: 264px; top: 166px; }
  .story--lead .story-title { left: 264px; top: 191px; font-size: 19px; line-height: 21px; }
  .story--lead .story-excerpt { left: 264px; top: 250px; width: 374px; }
  .story--lead .story-byline { left: 264px; top: 306px; }

  .story--tile .story-title { font-size: 14px; line-height: 17px; width: 260px; }
  .tile-a { left: 653px; top: 0; width: 284px; height: 166px; }
  .tile-b { left: 938px; top: 0; width: 262px; height: 166px; }
  .tile-c { left: 653px; top: 167px; width: 284px; height: 166px; }
  .tile-d { left: 938px; top: 167px; width: 262px; height: 166px; }
  .media-robot { background: linear-gradient(150deg, #77838c 0%, #5f6c77 60%, #4f5c68 100%); }
  .media-drone { background: linear-gradient(170deg, #4f6880 0%, #5f7f9c 60%, #7190a8 100%); }
  .story-grid::before { content: ""; position: absolute; left: 652px; top: 0; width: 548px; height: 333px; background: var(--divider); }

  .tile-a .story-date, .tile-b .story-date { top: 76px; }
  .tile-a .story-title, .tile-b .story-title { top: 89px; }
  .tile-a .story-byline, .tile-b .story-byline { top: 142px; }
  .tile-c .story-date, .tile-d .story-date { top: 79px; }
  .tile-c .story-title, .tile-d .story-title { top: 92px; }
  .tile-c .story-byline, .tile-d .story-byline { top: 147px; }
  .tile-a > *:not(.story-media), .tile-c > *:not(.story-media) { left: 18px; }
  .tile-b > *:not(.story-media), .tile-d > *:not(.story-media) { left: 20px; }
</style>
</head>
<body>
  <header class="site-header">
    <div class="brand">Logo</div>
    <nav class="main-nav">
      <a href="#" class="is-active">HOME</a>
      <a href="#" class="nav-news">NEWS</a>
      <a href="#" class="nav-about">ABOUT US</a>
      <a href="#" class="nav-contact">CONTACT US</a>
    </nav>
  </header>

  <main class="story-grid">
    <article class="story story--lead">
      <div class="story-media" role="img" aria-label="Photo of traders on a busy stock exchange floor with price boards"></div>
      <p class="story-date">April 23, 2015</p>
      <h1 class="story-title">Lorem ipsum dolor sit amet,<br>consectetur adipiscing elit.</h1>
      <p class="story-excerpt">Nunc aliquam euismod lectus. Lorem ipsum dolor sit amet, consectetur adipiscing elit. Suspendisse nec libero nibh. Ut non velit velit. Nulla id egestas felis. Fusce vestibulum lacinia enim.</p>
      <p class="story-byline">By <span>John Doe</span></p>
    </article>

    <article class="story story--tile tile-a">
      <div class="story-media media-robot" role="img" aria-label="Photo of a white humanoid robot by a window"></div>
      <p class="story-date">April 23, 2015</p>
      <h2 class="story-title">Lorem ipsum dolor sit amet,<br>consectetur adipiscing elit.</h2>
      <p class="story-byline">By <span>John Doe</span></p>
    </article>

    <article class="story story--tile tile-b">
      <div class="story-media media-drone" role="img" aria-label="Photo of a quadcopter drone with a camera against the sky"></div>
      <p class="story-date">April 23, 2015</p>
      <h2 class="story-title">Lorem ipsum dolor sit amet,<br>consectetur adipiscing elit.</h2>
      <p class="story-byline">By <span>John Doe</span></p>
    </article>

    <article class="story story--tile tile-c">
      <div class="story-media media-drone" role="img" aria-label="Photo of a quadcopter drone with a camera against the sky"></div>
      <p class="story-date">April 23, 2015</p>
      <h2 class="story-title">Lorem ipsum dolor sit amet,<br>consectetur adipiscing elit.</h2>
      <p class="story-byline">By <span>John Doe</span></p>
    </article>

    <article class="story story--tile tile-d">
      <div class="story-media media-robot" role="img" aria-label="Photo of a white humanoid robot by a window"></div>
      <p class="story-date">April 23, 2015</p>
      <h2 class="story-title">Lorem ipsum dolor sit amet,<br>consectetur adipiscing elit.</h2>
      <p class="story-byline">By <span>John Doe</span></p>
    </article>
  </main>
</body>
</html>
```